Business Card for By Karel Voss

Looking to have a business card designed for my lifestyle and fitness company. My company offers personal training, online programming and nutrition advice based out of London, United Kingdom.

I'd like to see modern, sleek designs, focusing on black, matte black or matte grey. Design doesn't need to be overly descriptive as this will also be used as a personal business card. I've included my logo.

Please note that my company is no longer called "Fitness by Karel Voss" but instead "By Karel Voss", this is because of my other ventures. Therefore please don't use the "fitness by karel voss" text.

information about my company can be found at www.bykarelvoss.com

Company is also based out of London (United Kingdom) & Sydney (Australia) this could be reflected on the card.

Industry/Entity Type

Business

Contact Information for Business Card

Karel Voss
+44 7382 615027
karel@bykarelvoss.com
www.bykarelvoss.com

Font styles to use
Sans Serif

Requirements
Must have
• All contact details and inclusion of my logo.

```html
<!DOCTYPE html>
<html lang="en">
<head>
<meta charset="utf-8">
<title>By Karel Voss — Business Card</title>
<link href="https://fonts.googleapis.com/css2?family=Montserrat:wght@500;600&family=Quicksand:wght@500&display=swap" rel="stylesheet">
<style>
  :root {
    --backdrop: #ece9e5;
    --matte-black: #1b1d1c;
    --matte-grey: #e3e3e3;
    --rule-grey: #cfcfcf;
    --ink-white: #ffffff;
  }
  html, body {
    margin: 0;
    padding: 0;
    width: 1200px;
    height: 799px;
    overflow: hidden;
    background: var(--backdrop);
  }
  .canvas {
    position: relative;
    width: 1200px;
    height: 799px;
  }
  .card {
    position: absolute;
    top: 283px;
    width: 445px;
    height: 248px;
    overflow: hidden;
    box-shadow: 0 2px 6px rgba(0,0,0,0.18);
  }
  .card--front { left: 139px; }
  .card--back { left: 624px; }
  .card__shapes {
    position: absolute;
    inset: 0;
    width: 100%;
    height: 100%;
    display: block;
  }

  /* front */
  .brand-mark {
    position: absolute;
    left: 196px;
    top: 76px;
    width: 56px;
    height: 56px;
    box-sizing: border-box;
    border: 3px solid var(--ink-white);
    border-radius: 50%;
  }
  .wordmark {
    position: absolute;
    left: 237px;
    top: 170px;
    transform: translate(-50%, -50%) rotate(-11deg);
    margin: 0;
    font-family: "Montserrat", sans-serif;
    font-weight: 600;
    font-size: 16px;
    letter-spacing: 2.5px;
    color: var(--ink-white);
    white-space: nowrap;
    text-transform: uppercase;
  }

  /* back */
  .holder-name {
    position: absolute;
    left: 113px;
    top: 50px;
    margin: 0;
    line-height: 24px;
    transform: rotate(-12deg);
    transform-origin: left bottom;
    font-family: "Montserrat", sans-serif;
    font-weight: 500;
    font-size: 19px;
    letter-spacing: 2.5px;
    text-transform: uppercase;
    white-space: nowrap;
  }
  .holder-name__first { color: var(--ink-white); }
  .holder-name__last { color: var(--matte-black); margin-left: 18px; }

  .contact-line {
    position: absolute;
    margin: 0;
    line-height: 12px;
    transform: rotate(-12deg);
    transform-origin: left bottom;
    font-family: "Quicksand", sans-serif;
    font-weight: 500;
    font-size: 9.5px;
    color: var(--matte-black);
    white-space: nowrap;
  }
  .contact-line--email { left: 243px; top: 145px; }
  .contact-line--phone { left: 245px; top: 178px; }
  .contact-line--web   { left: 261px; top: 200px; }

  .contact-icon {
    position: absolute;
    width: 18px;
    height: 14px;
  }
  .contact-icon--email { left: 206px; top: 158px; }
  .contact-icon--phone { left: 214px; top: 183px; }
  .contact-icon--web   { left: 221px; top: 211px; }
</style>
</head>
<body>
<main class="canvas">

  <section class="card card--front" aria-label="Business card front">
    <svg class="card__shapes" viewBox="0 0 377 210" preserveAspectRatio="none" aria-hidden="true">
      <rect width="377" height="210" fill="var(--matte-black)"/>
      <polygon points="0,0 130,0 145,57 0,93" fill="var(--matte-grey)"/>
      <polygon points="255,153 377,118 377,210 265,210" fill="var(--matte-grey)"/>
    </svg>
    <span class="brand-mark" aria-hidden="true"></span>
    <p class="wordmark">By Karel Voss</p>
  </section>

  <section class="card card--back" aria-label="Business card back">
    <svg class="card__shapes" viewBox="0 0 377 210" preserveAspectRatio="none" aria-hidden="true">
      <rect width="377" height="210" fill="var(--matte-grey)"/>
      <polygon points="0,0 158,0 216,210 0,210" fill="var(--matte-black)"/>
      <line x1="171" y1="51" x2="328" y2="13" stroke="var(--matte-black)" stroke-width="2.4"/>
      <line x1="34" y1="135" x2="187" y2="100" stroke="var(--rule-grey)" stroke-width="2.4"/>
    </svg>

    <h1 class="holder-name">
      <span class="holder-name__first">Karel</span><span class="holder-name__last">Voss</span>
    </h1>

    <svg class="contact-icon contact-icon--email" viewBox="0 0 18 14" aria-hidden="true">
      <rect x="1.5" y="1.5" width="15" height="11" fill="none" stroke="var(--ink-white)" stroke-width="1.6"/>
      <polyline points="1.5,1.5 9,8 16.5,1.5" fill="none" stroke="var(--ink-white)" stroke-width="1.4"/>
    </svg>
    <svg class="contact-icon contact-icon--phone" viewBox="0 0 18 14" aria-hidden="true">
      <path d="M5 1 q-3 2 0 7 q4 5.5 9 5.5 l1.5 -2.5 l-3.5 -2 l-1.5 1.3 q-2.5 -1.2 -3.5 -3.6 l1.3 -1.4 l-1.8 -3.6 z" fill="var(--ink-white)"/>
    </svg>
    <svg class="contact-icon contact-icon--web" viewBox="0 0 18 14" aria-hidden="true">
      <g fill="none" stroke="var(--ink-white)" stroke-width="1.6" stroke-linecap="round">
        <path d="M2 5 q7 -6 14 0"/>
        <path d="M5 8 q4 -3.5 8 0"/>
      </g>
      <circle cx="9" cy="11.5" r="1.5" fill="var(--ink-white)"/>
    </svg>

    <p class="contact-line contact-line--email">karel@bykarelvoss.com</p>
    <p class="contact-line contact-line--phone">+44 7382 615027</p>
    <p class="contact-line contact-line--web">www.bykarelvoss.com</p>
  </section>

</main>
</body>
</html>
```